TRV Mechanical Solutions Business Card Design

Business card design

Thinking just large logo on one side with a phone number and the back side is contact info with services we offer with a industrial plant across the bottom of the card

See must haves. I will be laser etching these business cards on black metal business cards as well as full color card stock. So must be bold and professional.

Target Market(s)

Industrial manufacturing

Contact Information for Business Card

Industrial manufacturing construction business specializing in consulting project managment and completing projects turn key

Font styles to use
Other font styles liked:
• See Logo for colors and font style

Requirements
Must have
• TRV Mechanical Solutions
• Gerald Munty
• 4821 Calloway Lane
• Harlow Creek, MD, 21094
• Project Managment
• Consulting
• Turn Key Industrial Projects
• I’d like a industrial manufacturing “cityline” on the back side bottom of the
• I’d like to be able to print these business cards in regular color on card stock but I’d also like the design to be etched into black metal business cards

```html
<!DOCTYPE html>
<html lang="en">
<head>
<meta charset="utf-8">
<title>TRV Mechanical Solutions – Business Cards</title>
<link rel="stylesheet" href="https://fonts.googleapis.com/css2?family=Audiowide&display=swap">
<style>
  :root {
    --page-bg: #3a3a3c;
    --card-bg: #0b0b0c;
    --card-glow: #26272a;
    --brand-blue: #2f5fbf;
    --text-white: #f2f2f2;
    --rule-grey: #4a4b4e;
  }
  * { margin: 0; padding: 0; box-sizing: border-box; }
  html, body {
    width: 1200px; height: 1000px; overflow: hidden;
    background: var(--page-bg);
    font-family: "Audiowide", sans-serif;
  }
  .card {
    position: absolute;
    width: 560px; height: 320px;
    background: radial-gradient(ellipse at 50% 25%, var(--card-glow) 0%, var(--card-bg) 65%);
    border-radius: 4px;
    box-shadow: 0 10px 30px rgba(0,0,0,.5);
    overflow: hidden;
  }
  .card--front { left: 90px; top: 110px; }
  .card--back  { left: 550px; top: 560px; }

  .brand-name {
    position: absolute; left: 0; right: 0;
    color: var(--brand-blue);
    text-align: center;
    line-height: 1.05;
    letter-spacing: 1px;
  }
  .brand-rule { position: absolute; height: 1px; background: var(--rule-grey); }

  .card--front .brand-name { top: 66px; font-size: 40px; }
  .card--front .brand-rule { left: 130px; right: 130px; top: 170px; }

  .phone {
    position: absolute; left: 0; right: 0; top: 206px;
    display: flex; justify-content: center; align-items: center; gap: 12px;
    color: var(--brand-blue); font-size: 26px; letter-spacing: 2px;
  }
  .phone svg { width: 26px; height: 26px; }

  .card--back .brand-name { top: 20px; font-size: 26px; }
  .card--back .brand-rule { left: 170px; right: 170px; top: 86px; }

  .contact {
    position: absolute; left: 24px; top: 112px; width: 250px;
    text-align: right;
  }
  .contact__name { color: var(--brand-blue); font-size: 18px; letter-spacing: 1px; margin-bottom: 8px; }
  .contact__line { color: var(--text-white); font-size: 12px; line-height: 1.5; }

  .divider {
    position: absolute; left: 290px; top: 108px; width: 2px; height: 66px;
    background: var(--brand-blue);
  }

  .services { position: absolute; left: 306px; top: 106px; }
  .services__title { color: var(--brand-blue); font-size: 14px; letter-spacing: 1px; margin-bottom: 4px; }
  .services__list { list-style: none; }
  .services__list li {
    color: var(--text-white); font-size: 11px; line-height: 1.55;
    display: flex; align-items: center; gap: 6px;
  }
  .services__list li::before {
    content: ""; width: 6px; height: 6px; background: var(--brand-blue);
  }

  .cityline {
    position: absolute; left: 0; right: 0; bottom: 0; height: 100px;
    background: linear-gradient(to top, var(--brand-blue) 0%, var(--brand-blue) 55%, rgba(47,95,191,.55) 100%);
  }
</style>
</head>
<body>
  <section class="card card--front" aria-label="Card front">
    <div class="brand-name">TRV Mechanical<br>Solutions</div>
    <div class="brand-rule"></div>
    <div class="phone">
      <svg viewBox="0 0 24 24" fill="none" stroke="currentColor" stroke-width="1.8">
        <circle cx="12" cy="12" r="10.5"/>
        <path d="M8.5 6.5l2 2.2-1.2 1.6c.8 1.7 2 2.9 3.7 3.7l1.6-1.2 2.2 2-1.3 1.7c-3.8-.6-7.1-3.9-7.7-7.7z" fill="currentColor" stroke="none"/>
      </svg>
      <span class="phone__number">55 318 4072</span>
    </div>
  </section>

  <section class="card card--back" aria-label="Card back">
    <div class="brand-name">TRV Mechanical<br>Solutions</div>
    <div class="brand-rule"></div>
    <div class="contact">
      <p class="contact__name">GERALD MUNTY</p>
      <p class="contact__line">4821 Calloway Lane</p>
      <p class="contact__line">Harlow Creek, MD, 21094</p>
    </div>
    <div class="divider"></div>
    <div class="services">
      <p class="services__title">SERVICES WE OFFER</p>
      <ul class="services__list">
        <li>Project Managment</li>
        <li>Consulting</li>
        <li>Turn Key Industrial Projects</li>
      </ul>
    </div>
    <div class="cityline" role="img" aria-label="Industrial plant skyline silhouette with cooling towers and smokestacks"></div>
  </section>
</body>
</html>
```